Join Our Real Estate Team

I would like to purchase a customized version of a design you have previously submitted - https://www.artpitchly.com/design/61937402

I want to create a recruitment AD. I have attached a AD I have created and would like as much of this information on an AD as possible. My main GOAL is to promote $350 Flat Fee (Includes E&O) per Transaction & No Monthly Fees.
I like to use a photo stock as I have in the attachment of various people.
I DON'T want to say "Wanted". Prefer to say something like "STOP Paying High Splits...Keep Most of YOUR hard earned Commissions"
Feel free to use other formats that might fit all the information that I have in my flyer I have uploaded.

Target Market(s)

Realtors

Industry/Entity Type

Real Estate

Font styles to use
Serif

Colors
0094D4
00A9DD
6FCCEA
C7EBF8
E9F6FB

Requirements
Must have
• See uploaded flyer to get must haves
Nice to have
• See uploaded flyer to get ideas
Should not have
• Do not want it to say "wanted"

```html
<!DOCTYPE html>
<html lang="en">
<head>
<meta charset="utf-8">
<title>Coastal Key Realty Group – Recruitment Flyer</title>
<link rel="stylesheet" href="https://fonts.googleapis.com/css2?family=Anton&family=Open+Sans:wght@400;600;700;800&display=swap">
<style>
  :root {
    --teal: #08959f;
    --teal-light: #5ec7cf;
    --blue: #0a97d9;
    --blue-bright: #00a9dd;
    --ink: #4a4a4a;
    --paper: #ffffff;
    --backdrop: #b4b4b4;
    --mist: #eef1f3;
  }
  html, body { margin: 0; padding: 0; }
  body {
    width: 977px; height: 1200px; overflow: hidden;
    background: var(--backdrop);
    position: relative;
    font-family: "Open Sans", Arial, sans-serif;
  }
  .flyer {
    position: absolute; left: 77px; top: 19px;
    width: 1141px; height: 1614px;
    transform: scale(0.72); transform-origin: 0 0;
    background: linear-gradient(180deg, var(--paper) 46%, var(--mist) 70%, var(--paper) 84%);
    box-shadow: 0 6px 20px rgba(0,0,0,.25);
    overflow: hidden;
  }
  .abs { position: absolute; }
  .team-photo {
    left: 0; top: 0; width: 1141px; height: 741px;
    background: linear-gradient(180deg, #d9dde2 0%, #b9c2cc 45%, #6c7a8c 100%);
  }
  .brand-badge {
    left: 381px; top: -141px; width: 354px; height: 354px;
    border-radius: 50%; background: var(--paper);
    box-shadow: 0 0 0 2px var(--paper), inset 0 0 0 14px var(--paper), inset 0 0 0 16px var(--teal);
    display: flex; align-items: flex-end; justify-content: center;
  }
  .brand-name {
    margin-bottom: 62px; font-weight: 700; font-size: 24px;
    color: var(--teal); text-align: center; line-height: 1.2;
  }
  .license-tag {
    left: 774px; top: 42px; width: 367px; height: 58px;
    background: var(--teal-light); color: #fff;
    border-radius: 29px 0 0 29px;
    font-weight: 700; font-size: 26px; line-height: 58px; text-align: center;
  }
  .headline {
    left: 0; width: 1141px; top: 770px; text-align: center;
    font-family: "Anton", Impact, sans-serif; font-size: 132px; line-height: 1;
    color: var(--teal); letter-spacing: 1px;
    text-shadow: -3px -3px 0 #fff, 3px 3px 0 #7fd2d7;
  }
  .subline {
    left: 0; width: 1141px; top: 912px; text-align: center;
    font-weight: 700; font-size: 27px; color: var(--ink);
  }
  .perks {
    left: 211px; top: 965px; width: 720px; height: 59px;
    border-radius: 30px; background: var(--teal-light); overflow: hidden;
    display: flex; align-items: center;
  }
  .perks-lead {
    height: 100%; width: 285px; background: var(--blue-bright);
    border-radius: 30px; color: #fff;
    font-family: "Anton", Impact, sans-serif; font-size: 34px;
    display: flex; align-items: center; justify-content: center;
  }
  .perks-lead sup { font-size: 16px; }
  .perks-rest { flex: 1; text-align: center; color: #fff; font-weight: 600; font-size: 23px; }
  .pitch {
    left: 215px; top: 1058px; width: 707px; height: 120px;
    border: 2px solid var(--teal); border-radius: 12px;
    color: var(--ink); font-weight: 600; font-size: 29px; line-height: 40px;
    text-align: center; display: flex; flex-direction: column; justify-content: center;
  }
  .pitch-mark {
    position: absolute; left: 50%; transform: translateX(-50%);
    background: var(--paper); padding: 0 10px;
    color: var(--teal); font-family: "Anton", Impact, sans-serif; font-size: 34px; line-height: 34px;
  }
  .pitch-mark.open { top: -18px; }
  .pitch-mark.close { bottom: -20px; background: var(--mist); }
  .example {
    left: 0; width: 1141px; top: 1205px; text-align: center;
    font-weight: 800; font-size: 27px; line-height: 39.5px;
  }
  .example .blue { color: var(--blue); }
  .example .teal { color: var(--teal); }
  .question-band {
    left: 0; top: 1334px; width: 1141px; height: 96px; background: var(--teal);
    color: #fff; font-weight: 600; font-size: 27px; line-height: 37px; text-align: center;
    display: flex; flex-direction: column; justify-content: center;
  }
  .contact-footer { left: 0; top: 1430px; width: 1141px; height: 168px; background: var(--paper); }
  .phone-pill {
    left: 47px; top: 41px; width: 350px; height: 55px; border-radius: 28px;
    background: var(--teal); color: #fff; font-weight: 700; font-size: 40px;
    display: flex; align-items: center; justify-content: center; gap: 12px;
  }
  .website { left: 47px; width: 350px; top: 106px; text-align: center; font-size: 19px; color: var(--ink); }
  .website b { color: var(--teal); font-weight: 600; }
  .divider { top: 36px; width: 2px; height: 95px; background: var(--teal); }
  .agent { left: 426px; width: 324px; top: 50px; text-align: center; }
  .agent-name { color: var(--teal); font-weight: 600; font-size: 23px; }
  .agent-email { color: var(--teal); font-weight: 600; font-size: 23px; margin-top: 6px; }
  .join {
    left: 760px; width: 360px; top: 26px; text-align: center;
    font-family: "Anton", Impact, sans-serif; font-size: 30px; line-height: 40px; color: var(--teal);
  }
  .broker-tag {
    left: 804px; top: 104px; width: 270px; height: 36px; box-sizing: border-box;
    border: 2px solid var(--teal); border-radius: 18px;
    color: var(--teal); font-weight: 700; font-size: 16px; line-height: 32px; text-align: center;
  }
  .base-bar { left: 0; top: 1598px; width: 1141px; height: 16px; display: flex; }
  .base-bar span:first-child { width: 567px; background: var(--blue); }
  .base-bar span:last-child { flex: 1; background: var(--teal-light); }
</style>
</head>
<body>
  <main class="flyer">
    <div class="abs team-photo" role="img" aria-label="Stock photo of a smiling, diverse group of real estate professionals standing with arms crossed in a bright office"></div>

    <div class="abs brand-badge">
      <div class="brand-name">COASTAL KEY<br>REALTY GROUP</div>
    </div>
    <div class="abs license-tag">Bk4417203 / CQ2086571</div>

    <h1 class="abs headline" style="margin:0">$350 Flat Fee</h1>
    <p class="abs subline" style="margin:0">(Includes E&amp;O) Per Transaction &amp; No Monthly Fees</p>

    <div class="abs perks">
      <div class="perks-lead">Per transaction<sup>*</sup></div>
      <div class="perks-rest">No Monthly Fees Timely Payouts</div>
    </div>

    <blockquote class="abs pitch" style="margin:0">
      <span class="pitch-mark open">“</span>
      <span>Stop Paying high splits...</span>
      <span>keep most of your hard earned commissions</span>
      <span class="pitch-mark close">”</span>
    </blockquote>

    <div class="abs example">
      <div class="blue">On A $250,000 Sale w/3% commission</div>
      <div class="blue">$350 Flat Fee = $7,150</div>
      <div class="teal">Commission Earned w/CKRG</div>
    </div>

    <div class="abs question-band">
      <span>Are You frustrated giving up</span>
      <span>20%,30% or even 50% of your commission???</span>
    </div>

    <footer class="abs contact-footer">
      <div class="abs phone-pill">
        <svg width="30" height="30" viewBox="0 0 30 30" aria-hidden="true">
          <circle cx="15" cy="15" r="13" fill="#fff"/>
          <path d="M10 8.5l3 .2 1 4-2 1.3c.9 2 2.3 3.4 4.2 4.2l1.3-2 4 1 .2 3c-.6 1-2 1.6-3.5 1.3C12.5 20.5 9.5 17.4 8.4 12c-.3-1.5.4-3 1.6-3.5z" fill="var(--teal)"/>
        </svg>
        <span>555.201.4470</span>
      </div>
      <div class="abs website">
        <svg width="18" height="18" viewBox="0 0 18 18" aria-hidden="true" style="vertical-align:-3px">
          <circle cx="9" cy="9" r="7.5" fill="none" stroke="var(--teal)" stroke-width="1.5"/>
          <path d="M1.5 9h15M9 1.5c-3 3.5-3 11.5 0 15M9 1.5c3 3.5 3 11.5 0 15" fill="none" stroke="var(--teal)" stroke-width="1.2"/>
        </svg>
        www.<b>CoastalKeyRealtyGroup</b>.com
      </div>

      <div class="abs divider" style="left:424px"></div>

      <div class="abs agent">
        <div class="agent-name">DANA WELLS</div>
        <div class="agent-email">
          <svg width="20" height="20" viewBox="0 0 20 20" aria-hidden="true" style="vertical-align:-3px">
            <circle cx="10" cy="10" r="9" fill="var(--teal)"/>
            <rect x="5" y="6.5" width="10" height="7" rx="1" fill="#fff"/>
            <path d="M5.5 7l4.5 3.5L14.5 7" fill="none" stroke="var(--teal)" stroke-width="1.2"/>
          </svg>
          Dana@CoastalKeyRG.com
        </div>
      </div>

      <div class="abs divider" style="left:750px"></div>

      <div class="abs join">Join Our Team Start Earning<br>More Today!</div>
      <div class="abs broker-tag">Your “Dana”mic Broker</div>
    </footer>

    <div class="abs base-bar"><span></span><span></span></div>
  </main>
</body>
</html>
```